Clever Cargo Trike Ad Campaign

I've started a cargo trike company in Washington, DC that will generate revenue from deliveries, promotions and advertising. The trikes have three large ad panel spaces that are perfect for banners. While I'll be using these for promoting customer products/services, I'd like a creative ad that also promotes my own company when not promoting others.

The trikes are human pedal powered, with electric-assist. They can carry 550 lbs and 62 cubic feet of cargo anywhere in DC's downtown area. They make no noise, don't block streets while delivering goods, move around town as quickly as vans or trucks, have zero tailipipe emissions, can use bike lanes, reduce street congestion, etc. In shortly, they are eco-friendly, low-impact, socially-responsible, dependable and efficient!

I'd also like to convey that the trikes are available for advertising and promotional campaigns.....

I'd like a campaign that conveys some of the above, but in a clever, (maybe even humorous) fashion. Not sure if each of three panels (54"x30", 54"x30", 37"x33") needs same ad or just similar ones. Campaign should be geared toward potential customers (organic drycleaners, bakeries, office supply, caterers, farmshare food deliveries, etc), but also be pertinent to anyone who views.

I've included our company logo and a graphic I created that shows the DC skyline (as yet unused). Also included a photo of one of the trikes.

Target Market(s)

* Businesses within Washington, DC that are seeking a unique delivery service.
* Large/small businesses seeking a dedicated, effective ad campaign venue in DC
* Any business seeking to promote products/services (hand out samples or brochures, represent them a street fairs, etc.)

Industry/Entity Type

It Company

Requirements
Must have
• I can easily come up with my own plain, straightforward ad campaign. I'm looking for something creative, unique, attractive that doesn't overwhelm the customer with information. I want it to convey what we have to offer potential customers.
Nice to have
• It would be great it if were humorous, had some kind of Washington focus, etc. But these are not crucial. While I'd like to somehow address the "eco-friendly" aspect of the company, I don't want this to be the sole focus.
• Thus, we can use colors other than the green in my logo, as long as they go well with what I have.
Should not have
• While I'm no fan of today's DC political environment, I don't want a campaign that will bring adverse attention to my company.

```html
<!DOCTYPE html>
<html lang="en">
<head>
<meta charset="utf-8">
<title>We Deliver – Pedalpost</title>
<link rel="stylesheet" href="https://fonts.googleapis.com/css2?family=Anton&display=swap">
<style>
  :root {
    --brand-green: #389a40;
    --paper: #ffffff;
  }
  html, body {
    margin: 0;
    padding: 0;
    overflow: hidden;
    background: var(--paper);
  }
  .ad-panel {
    position: relative;
    width: 1200px;
    height: 666px;
    background: var(--paper);
    overflow: hidden;
    font-family: "Anton", "Impact", sans-serif;
    color: var(--brand-green);
  }
  .headline {
    position: absolute;
    left: 0;
    top: 168px;
    width: 1200px;
    margin: 0;
    text-align: center;
    font-size: 168px;
    line-height: 1;
    font-weight: 400;
    letter-spacing: 6px;
    text-transform: uppercase;
  }
  .tagline {
    position: absolute;
    left: 0;
    top: 334px;
    width: 1200px;
    margin: 0;
    text-align: center;
    font-size: 66px;
    line-height: 1;
    font-weight: 400;
    letter-spacing: 4px;
    text-transform: uppercase;
  }
  .brand {
    position: absolute;
    left: 0;
    top: 528px;
    width: 1200px;
    display: flex;
    justify-content: center;
    align-items: center;
    gap: 18px;
  }
  .brand-name {
    font-size: 52px;
    line-height: 1;
    font-weight: 400;
    letter-spacing: 2px;
    text-transform: uppercase;
  }
  .brand-dot {
    width: 40px;
    height: 40px;
    display: block;
  }
</style>
</head>
<body>
  <main class="ad-panel">
    <h1 class="headline">We Deliver</h1>
    <p class="tagline">(Zero Emissions)</p>
    <div class="brand">
      <span class="brand-name">Pedalpost</span>
      <svg class="brand-dot" viewBox="0 0 40 40" aria-hidden="true">
        <circle cx="20" cy="20" r="20" fill="var(--brand-green)"/>
      </svg>
    </div>
  </main>
</body>
</html>
```